Long term design collaboration - mobile app design & web app design

We are looking for a talented mobile designer to help us improve our UI & UX for mobile app and web app.

The screens that need to be redesigned are attached.

There is potentially a lot more work in future design available for the successful candidate.
The successful candidate would have to take part in daily stand-up around 3 times per week.
The successful candidate would join a dev team
We are software company that does property management

```html
<!DOCTYPE html>
<html lang="en">
<head>
<meta charset="utf-8">
<title>Property management app screens</title>
<link href="https://fonts.googleapis.com/css2?family=Inter:wght@400;500;600;700&display=swap" rel="stylesheet">
<style>
:root{
  --bg:#e9edf4;
  --brand:#2a5bbd;
  --ink:#111418;
  --muted:#5b5f66;
  --line:#d9dce1;
  --white:#ffffff;
  --rose-bg:#fcf1f1;
  --rose:#e0474c;
  --mint-bg:#f1faf7;
  --mint:#4dbb9a;
  --chip:#ececec;
  --tile:#f7f7f7;
  --amber-bg:#fff4ea;
  --amber:#e3661b;
  --red-bg:#fdf0ef;
  --red:#c8332c;
}
*{box-sizing:border-box;margin:0;padding:0}
html,body{width:1200px;height:869px;overflow:hidden}
body{background:var(--bg);font-family:'Inter',sans-serif;color:var(--ink);position:relative}
.screen{position:absolute;top:45px;width:360px;height:779px;background:var(--white);border-radius:12px;overflow:hidden;box-shadow:0 6px 24px rgba(20,30,60,.12)}
.screen--finances{left:35px}
.screen--wizard{left:420px}
.screen--overview{left:804px}
.appbar{height:53px;background:var(--brand);color:var(--white);display:flex;align-items:center;justify-content:space-between;padding:0 16px}
.appbar h1{font-size:16px;font-weight:700}
.appbar svg{width:20px;height:20px}
.abs{position:absolute}
.overline{font-size:11px;letter-spacing:1.2px;font-weight:500;left:15px}
.section-title{left:15px;right:16px;font-size:16px;font-weight:600;display:flex;justify-content:space-between;align-items:center}
.section-title svg{width:14px;height:14px}
.stat{position:absolute;width:156px;border-radius:8px;padding:12px}
.stat--rose{background:var(--rose-bg);height:110px}
.stat--mint{background:var(--mint-bg);height:116px}
.stat svg{width:20px;height:22px;display:block}
.stat .label{font-size:13px;color:var(--muted);margin-top:20px}
.stat .value{font-size:24px;font-weight:700;margin-top:3px}
.question{left:15px;top:71px;font-size:16px;font-weight:600}
.option{position:absolute;left:15px;width:329px;height:53px;border:1px solid var(--line);border-radius:6px;display:flex;align-items:center;padding-left:16px;font-size:14px;color:var(--muted)}
.radio{width:20px;height:20px;border:2px solid var(--ink);border-radius:50%;margin-right:14px;display:flex;align-items:center;justify-content:center}
.radio--on::after{content:"";width:10px;height:10px;border-radius:50%;background:var(--ink)}
.btn{position:absolute;top:701px;width:156px;height:45px;border-radius:6px;font-size:16px;font-weight:600;display:flex;align-items:center;justify-content:center}
.btn--ghost{left:15px;border:1px solid var(--brand);color:var(--brand)}
.btn--primary{left:188px;background:var(--brand);color:var(--white)}
.group-title{left:15px;font-size:16px;font-weight:600}
.info-list{position:absolute;left:15px;top:100px;width:329px;border:1px solid var(--line);border-radius:6px}
.info-row{height:61px;padding:9px 8px;display:flex;justify-content:space-between;align-items:center;border-bottom:1px solid var(--line)}
.info-row:last-child{border-bottom:0}
.info-row b{display:block;font-size:15px;font-weight:600}
.info-row span{display:block;font-size:15px;color:var(--muted);margin-top:6px}
.info-row svg{width:14px;height:14px}
.tile{position:absolute;width:137px;height:114px;background:var(--tile);border-radius:6px;padding:7px}
.tile--amber{background:var(--amber-bg)}
.tile--red{background:var(--red-bg)}
.chip{display:inline-flex;align-items:center;gap:6px;background:var(--chip);border-radius:5px;padding:3px 8px;font-size:15px}
.tile--amber .chip{background:#fde9d8;color:var(--amber)}
.tile--red .chip{background:#fbe0de;color:var(--red)}
.tile-card{margin-top:7px;background:var(--white);border-radius:5px;box-shadow:0 1px 4px rgba(0,0,0,.12);height:65px;padding:10px;font-size:13px}
.tile-card p+p{margin-top:12px}
.tile--red .tile-card p:first-child{color:var(--red)}
.tile--red .tile-card p+p{font-size:11px}
.navbar{position:absolute;left:0;right:0;bottom:0;height:80px;background:var(--white);display:flex;justify-content:space-around;padding:0 8px;box-shadow:0 -14px 18px rgba(0,0,0,.03)}
.nav-item{width:80px;display:flex;flex-direction:column;align-items:center;padding-top:17px;font-size:14px;color:var(--muted)}
.nav-item svg{width:20px;height:20px;margin-bottom:6px}
.nav-item--active{color:var(--brand);font-weight:600}
</style>
</head>
<body>

<svg width="0" height="0" style="position:absolute">
  <defs>
    <symbol id="i-back" viewBox="0 0 20 20"><path d="M17 10H3M9 4l-6 6 6 6" fill="none" stroke="currentColor" stroke-width="2" stroke-linecap="round" stroke-linejoin="round"/></symbol>
    <symbol id="i-menu" viewBox="0 0 20 20"><path d="M2 5h16M2 10h16M2 15h16" stroke="currentColor" stroke-width="2" stroke-linecap="round"/></symbol>
    <symbol id="i-chev" viewBox="0 0 14 14"><path d="M5 2l5 5-5 5" fill="none" stroke="currentColor" stroke-width="1.8" stroke-linecap="round" stroke-linejoin="round"/></symbol>
    <symbol id="i-receipt" viewBox="0 0 20 22"><path d="M3 1h14v19l-2.5-1.5L12 20l-2-1.5L8 20l-2.5-1.5L3 20z" fill="none" stroke="currentColor" stroke-width="2" stroke-linejoin="round"/><path d="M6 6h8M6 10h8M6 14h5" stroke="currentColor" stroke-width="2"/></symbol>
    <symbol id="i-list" viewBox="0 0 20 22"><rect x="2" y="2" width="16" height="18" rx="1" fill="currentColor"/><path d="M5 7h10M5 11h10M5 15h10" stroke="#fff" stroke-width="1.6"/></symbol>
    <symbol id="i-doc-cash" viewBox="0 0 20 22"><path d="M3 1h10l5 5v15H3z" fill="currentColor"/><text x="10.5" y="16" font-size="10" font-family="Inter,sans-serif" font-weight="700" fill="#fff" text-anchor="middle">$</text></symbol>
  </defs>
</svg>

<!-- Finances -->
<section class="screen screen--finances">
  <header class="appbar">
    <svg><use href="#i-back"/></svg><h1>Finances</h1><svg><use href="#i-menu"/></svg>
  </header>
  <p class="abs overline" style="top:70px">ACCOUNT RECEIVABLE</p>
  <div class="abs section-title" style="top:93px"><span>Arrears</span><svg><use href="#i-chev"/></svg></div>
  <div class="stat stat--rose" style="left:15px;top:123px"><svg style="color:var(--rose)"><use href="#i-list"/></svg><p class="label">Total</p><p class="value">£7,268.22</p></div>
  <div class="stat stat--rose" style="left:188px;top:123px"><svg style="color:var(--rose)"><use href="#i-receipt"/></svg><p class="label">Bills</p><p class="value">5</p></div>
  <div class="abs section-title" style="top:250px"><span>Unallocated Receipts</span><svg><use href="#i-chev"/></svg></div>
  <div class="stat stat--rose" style="left:15px;top:280px"><svg style="color:var(--rose)"><use href="#i-receipt"/></svg><p class="label">Total</p><p class="value">£7,268.22</p></div>
  <div class="stat stat--rose" style="left:188px;top:280px"><svg style="color:var(--rose)"><use href="#i-list"/></svg><p class="label">Receipts</p><p class="value">5</p></div>
  <p class="abs overline" style="top:423px">ACCOUNT RECEIVABLE</p>
  <div class="abs section-title" style="top:446px"><span>Invoices</span><svg><use href="#i-chev"/></svg></div>
  <div class="stat stat--mint" style="left:15px;top:478px"><svg style="color:var(--mint)"><use href="#i-doc-cash"/></svg><p class="label">Total</p><p class="value">£4,268.78</p></div>
  <div class="stat stat--mint" style="left:188px;top:478px"><svg style="color:var(--mint)"><use href="#i-receipt"/></svg><p class="label">Invoices</p><p class="value">5</p></div>
</section>

<!-- Legionellas wizard -->
<section class="screen screen--wizard">
  <header class="appbar">
    <svg><use href="#i-back"/></svg><h1>Legionellas</h1><svg><use href="#i-menu"/></svg>
  </header>
  <p class="abs question">Is it required?</p>
  <div class="option" style="top:100px"><span class="radio"></span>No</div>
  <div class="option" style="top:161px"><span class="radio"></span>Yes, but I do not have a file to upload</div>
  <div class="option" style="top:223px"><span class="radio radio--on"></span>Yes, and I have a file to upload</div>
  <div class="btn btn--ghost">Back</div>
  <div class="btn btn--primary">Next</div>
</section>

<!-- Overview -->
<section class="screen screen--overview">
  <header class="appbar">
    <svg><use href="#i-back"/></svg><h1>Overview</h1><svg><use href="#i-menu"/></svg>
  </header>
  <p class="abs group-title" style="top:71px">General</p>
  <div class="info-list">
    <div class="info-row"><div><b>Units</b><span>85</span></div><svg><use href="#i-chev"/></svg></div>
    <div class="info-row"><div><b>Handover Date</b><span>12 January 2023</span></div><svg><use href="#i-chev"/></svg></div>
    <div class="info-row"><div><b>Address</b><span>24 Marlow Crescent Avenue, Lo...</span></div><svg><use href="#i-chev"/></svg></div>
    <div class="info-row"><div><b>Section 20 limit</b><span>£20</span></div></div>
  </div>
  <p class="abs group-title" style="top:363px">Compliance</p>
  <div class="tile" style="left:15px;top:392px"><span class="chip">Asbestos</span><div class="tile-card"><p>NA</p><p>-</p></div></div>
  <div class="tile tile--amber" style="left:164px;top:392px"><span class="chip">Legionellas <svg width="18" height="18" viewBox="0 0 18 18"><circle cx="9" cy="9" r="8" fill="none" stroke="currentColor" stroke-width="1.6"/><path d="M6.8 7a2.2 2.2 0 1 1 3 2c-.6.3-.8.7-.8 1.3" fill="none" stroke="currentColor" stroke-width="1.6" stroke-linecap="round"/><circle cx="9" cy="13" r="1" fill="currentColor"/></svg></span><div class="tile-card"><p>-</p><p>-</p></div></div>
  <div class="tile tile--red" style="left:313px;top:392px"><span class="chip">Drains</span><div class="tile-card"><p>Overdue</p><p>10 Dec 2023</p></div></div>
  <p class="abs group-title" style="top:525px">Insurances</p>
  <div class="tile" style="left:15px;top:553px"><span class="chip">Terrorism</span><div class="tile-card"><p>NA</p><p>-</p></div></div>
  <div class="tile" style="left:164px;top:553px"><span class="chip">Buildings</span><div class="tile-card"><p>NA</p><p>-</p></div></div>
  <div class="tile" style="left:313px;top:553px"><span class="chip">Engineering</span><div class="tile-card"><p>NA</p><p>-</p></div></div>
  <nav class="navbar">
    <div class="nav-item nav-item--active"><svg viewBox="0 0 20 20"><path d="M3 9l7-6 7 6v8h-4v-5H7v5H3z" fill="none" stroke="currentColor" stroke-width="1.8" stroke-linejoin="round"/></svg>Home</div>
    <div class="nav-item"><svg viewBox="0 0 20 20"><rect x="2" y="2" width="16" height="16" rx="1.5" fill="none" stroke="currentColor" stroke-width="1.8"/><path d="M6 7h8M6 10h8M6 13h8" stroke="currentColor" stroke-width="1.6"/></svg>Overview</div>
    <div class="nav-item"><svg viewBox="0 0 20 20"><path d="M4 1.5h8l4 4v13H4z" fill="none" stroke="currentColor" stroke-width="1.8" stroke-linejoin="round"/><text x="10" y="15" font-size="9" font-weight="700" font-family="Inter,sans-serif" fill="currentColor" text-anchor="middle">$</text></svg>Finances</div>
    <div class="nav-item"><svg viewBox="0 0 20 20"><circle cx="10" cy="6" r="3.5" fill="none" stroke="currentColor" stroke-width="1.8"/><path d="M3 18c0-4 3-6 7-6s7 2 7 6z" fill="none" stroke="currentColor" stroke-width="1.8" stroke-linejoin="round"/></svg>Profile</div>
  </nav>
</section>

</body>
</html>
```